A Clear Three Step Roadmap For Contractors

We are looking for a one-pager "roadmap" that is similar to the 2nd picture we attached, but much more professional & better... please make it landscape orientation. The logo for this system is attached below, as well.

Our Brand Colors to use:
#f2d582
#303030
#8b8c90

The copy we'd like to use on the flyer:
A Clear Three Step Roadmap that will finally allow you to attract quality customers and win more jobs.

The Keystone Ladder Method is a simple to follow system that was created specifically for Contractors and Blue Collar Business Owners.

When it comes to marketing and growing their business, the majority of Contractors are left confused, frustrated and extremely overwhelmed. Unlike most sales, marketing & training programs that offer a single "piece of the puzzle", we've mapped out each essential step of the puzzle and cut out all of the fluff.

All you have to do is complete each step in the right order and we'll be guiding you along the entire journey!

A ---> B

Blueprint: Get clear on where you're going, define your ideal audience, and finally, master your message.
Step 1: Clarify The Chaos
Step 2: Define Your Customer
Step 3: Master Your Message

Build: Attract quality leads, Build your funnel and Formulate a high-converting follow-up system
Step 4: Develop Lead Generator
Step 5: Construct Your Funnel
Step 6: Formulate the Follow-Up

Breakthrough: Get in front of your ideal customers and rapidly scale your business by driving traffic and becoming the authority in your market
Step 7: Turn-On the Traffic
Step 8: Become the Authority
Step 9: Unlock Your Growth

```html
<!DOCTYPE html>
<html lang="en">
<head>
<meta charset="utf-8">
<title>Keystone Ladder Method – A Clear Three Step Roadmap</title>
<link href="https://fonts.googleapis.com/css2?family=Lato:ital,wght@0,400;0,700;0,900;1,700;1,900&display=swap" rel="stylesheet">
<style>
  :root{
    --gold:#f2d582;
    --gold-deep:#d9b65a;
    --charcoal:#303030;
    --charcoal-dark:#1f1f1f;
    --grey:#8b8c90;
    --ink:#1b1b1b;
    --white:#ffffff;
  }
  *{margin:0;padding:0;box-sizing:border-box}
  html,body{width:1200px;height:770px;overflow:hidden;background:#eeeeee}
  body{font-family:"Lato",sans-serif}
  .flyer{position:relative;width:1200px;height:770px;background:var(--charcoal);overflow:hidden}
  .flyer-art{position:absolute;inset:0}
  .brand{position:absolute;left:72px;top:58px;display:flex;align-items:center;gap:18px}
  .brand-mark{width:58px;height:58px;background:var(--gold)}
  .brand-name{font-weight:900;font-size:31px;line-height:1.05;color:var(--charcoal);letter-spacing:.5px;text-transform:uppercase}
  .headline{position:absolute;left:540px;width:640px;top:36px;text-align:center;color:var(--ink);font-style:italic;font-weight:900;text-transform:uppercase}
  .headline-main{font-size:41px;line-height:1.15;letter-spacing:-.3px}
  .headline-sub{font-size:27px;line-height:1.22;font-weight:700;margin-top:4px}
  .intro{position:absolute;left:74px;top:218px;width:1060px;color:var(--white);font-weight:700;font-size:15px;line-height:23px}
  .intro p{margin-bottom:13px}
  .intro .intro-last{width:470px}
  .steps{position:absolute;left:72px;top:448px;list-style:none}
  .step{display:flex;align-items:center;height:101px}
  .step-number{width:78px;height:78px;border-radius:50%;background:var(--white);border:3px solid var(--ink);box-shadow:0 0 0 5px var(--gold),0 0 0 7px var(--ink);display:flex;align-items:center;justify-content:center;font-weight:900;font-size:44px;color:var(--ink);flex:none}
  .step-body{margin-left:20px}
  .step-title{font-weight:900;font-size:37px;line-height:1;color:var(--ink);letter-spacing:.3px}
  .step-text{font-weight:700;font-size:11px;line-height:15px;color:var(--charcoal);margin-top:6px;width:340px}
</style>
</head>
<body>
<main class="flyer">
  <svg class="flyer-art" viewBox="0 0 1200 770" width="1200" height="770" aria-hidden="false">
    <defs>
      <linearGradient id="headerGold" x1="0" y1="0" x2="1" y2="0">
        <stop offset="0" stop-color="#d6b45a"/>
        <stop offset=".5" stop-color="#f2d582"/>
        <stop offset="1" stop-color="#dcbc66"/>
      </linearGradient>
      <linearGradient id="panelGold" x1="0" y1="0" x2="1" y2="1">
        <stop offset="0" stop-color="#f2d582"/>
        <stop offset="1" stop-color="#e9c86e"/>
      </linearGradient>
      <linearGradient id="screen" x1="0" y1="0" x2="1" y2="1">
        <stop offset="0" stop-color="#3a3a3a"/>
        <stop offset="1" stop-color="#1c1c1c"/>
      </linearGradient>
    </defs>
    <!-- header -->
    <rect class="header-band" x="0" y="0" width="1200" height="190" fill="url(#headerGold)"/>
    <polygon class="header-white" points="0,0 517,0 474,190 0,190" fill="var(--white)"/>
    <!-- lower gold sweep -->
    <path class="gold-sweep" d="M0,440 C110,405 250,392 340,404 C470,422 560,470 660,520 C820,600 980,660 1200,679 L1200,770 L0,770 Z" fill="url(#panelGold)"/>
    <!-- tablet frame -->
    <rect class="tablet-frame" x="585" y="327" width="539" height="415" rx="22" fill="var(--white)" stroke="#d8c89a" stroke-width="3"/>
    <circle cx="607" cy="535" r="3" fill="var(--charcoal)"/>
    <circle cx="1096" cy="535" r="13" fill="none" stroke="#c9c9c9" stroke-width="1.5"/>
    <rect class="tablet-screen" x="636" y="347" width="433" height="369" fill="url(#screen)"/>
    <!-- roadmap grid connectors -->
    <g stroke="#9a9a9a" stroke-width="1" stroke-dasharray="4 3">
      <line x1="705" y1="441" x2="1005" y2="441"/>
      <line x1="705" y1="528" x2="1005" y2="528"/>
      <line x1="705" y1="620" x2="1005" y2="620"/>
    </g>
    <g fill="#ececec" stroke="var(--gold)" stroke-width="2">
      <circle cx="777" cy="441" r="22"/><circle cx="893" cy="441" r="22"/><circle cx="1005" cy="441" r="22"/>
      <circle cx="777" cy="528" r="22"/><circle cx="893" cy="528" r="22"/><circle cx="1005" cy="528" r="22"/>
      <circle cx="777" cy="620" r="22"/><circle cx="893" cy="620" r="22"/><circle cx="1005" cy="620" r="22"/>
    </g>
    <g font-family="Lato, sans-serif" font-size="7" fill="var(--gold)" text-anchor="middle">
      <text x="777" y="410">Turn-On the Traffic</text>
      <text x="893" y="410">Become the Authority</text>
      <text x="1005" y="410">Unlock Your Growth</text>
      <text x="777" y="497">Formulate the Follow-Up</text>
      <text x="893" y="497">Construct Your Funnel</text>
      <text x="1005" y="497">Develop Lead Generator</text>
      <text x="777" y="589">Clarify the Chaos</text>
      <text x="893" y="589">Define Your Customer</text>
      <text x="1005" y="589">Master Your Message</text>
    </g>
    <g font-family="Lato, sans-serif" font-weight="700" font-size="10" fill="var(--white)">
      <rect x="649" y="433" width="14" height="16" fill="var(--white)"/><text x="652" y="445" fill="var(--ink)">3</text>
      <text x="669" y="445">BREAKTHROUGH</text>
      <rect x="649" y="520" width="14" height="16" fill="var(--white)"/><text x="652" y="532" fill="var(--ink)">2</text>
      <text x="669" y="532">BUILD</text>
      <rect x="649" y="612" width="14" height="16" fill="var(--white)"/><text x="652" y="624" fill="var(--ink)">1</text>
      <text x="669" y="624">BLUEPRINT</text>
    </g>
    <g stroke="var(--gold)" stroke-width="1.5">
      <line x1="669" y1="449" x2="735" y2="449"/><line x1="669" y1="536" x2="702" y2="536"/><line x1="669" y1="628" x2="722" y2="628"/>
      <line x1="1028" y1="430" x2="1050" y2="420"/>
    </g>
    <g font-family="Lato, sans-serif" font-style="italic" font-weight="700" font-size="16" fill="var(--gold)">
      <text x="740" y="662">A</text>
      <text x="1054" y="422">B</text>
    </g>
    <text x="1062" y="709" text-anchor="end" font-family="Lato, sans-serif" font-size="8" fill="var(--white)">Keystone Ladder Method ©</text>
  </svg>

  <div class="brand">
    <span class="brand-mark"></span>
    <span class="brand-name">Keystone Ladder<br>Method</span>
  </div>

  <header class="headline">
    <h1 class="headline-main">A Clear Three Step Roadmap</h1>
    <p class="headline-sub">That will finally allow you to attract<br>quality customers and win more jobs.</p>
  </header>

  <section class="intro">
    <p>The Keystone Ladder Method is a simple to follow system that was created specifically for Contractors and Blue Collar Business Owners</p>
    <p>When it comes to growing their business, the majority of Contractors are left confused, frustrated and extremely overwhelmed. Unlike most sales, marketing &amp; training programs that offer a single "piece of the puzzle", we've mapped out each essential step of the puzzle and cut out all of the fluff.</p>
    <p class="intro-last">All you have to do is complete each step in the right order and we'll be guiding you along the entire journey!</p>
  </section>

  <ol class="steps">
    <li class="step">
      <span class="step-number">1</span>
      <div class="step-body">
        <h2 class="step-title">BLUEPRINT</h2>
        <p class="step-text">Get clear on where you're going, define your ideal audience, and finally master your message</p>
      </div>
    </li>
    <li class="step">
      <span class="step-number">2</span>
      <div class="step-body">
        <h2 class="step-title">BUILD</h2>
        <p class="step-text">Attract quality leads, Build your funnel and Formulate a high-converting follow-up system</p>
      </div>
    </li>
    <li class="step">
      <span class="step-number">3</span>
      <div class="step-body">
        <h2 class="step-title">BREAKTHROUGH</h2>
        <p class="step-text">Get in front of your ideal customers and rapidly scale your business by driving traffic and becoming the authority in your market</p>
      </div>
    </li>
  </ol>
</main>
</body>
</html>
```